Bramblewood Lodging letterhead

We need a letterhead designed that includes the new logo that has just been designed for our business. The letterhead will need to be formatted for digital use as well as for print.

Target Market(s)

Private tenant, corporate tenants, real estate agents

Industry/Entity Type

Digital

Requirements
Must have
• ABN 87 592 104 316
PO Box 7816, Tilbury Mail Centre QLD 4792
Email: dorian.platt@quillmail.net
Ph: 0438 172 964

```html
<!DOCTYPE html>
<html lang="en">
<head>
<meta charset="utf-8">
<title>Bramblewood Lodging Letterhead</title>
<link rel="stylesheet" href="https://fonts.googleapis.com/css2?family=Quicksand:wght@600;700&display=swap">
<style>
  :root {
    --maroon: #5a0a2a;
    --ink: #6a1426;
    --paper: #ffffff;
    --frame: #8a8a8a;
    --mark-faint: #f3eeee;
  }
  * { margin: 0; padding: 0; box-sizing: border-box; }
  html, body {
    width: 849px;
    height: 1200px;
    overflow: hidden;
    background: var(--paper);
  }
  .letterhead {
    position: relative;
    width: 849px;
    height: 1200px;
    background: var(--paper);
    border: 1px solid var(--frame);
    overflow: hidden;
    font-family: "Quicksand", sans-serif;
  }
  .top-arc {
    position: absolute;
    top: 0;
    left: 0;
    width: 849px;
    height: 120px;
  }
  .brand {
    position: absolute;
    left: 28px;
    top: 124px;
    display: flex;
    align-items: center;
    gap: 12px;
  }
  .brand-square {
    width: 64px;
    height: 64px;
    border-radius: 6px;
    background: var(--maroon);
  }
  .brand-name {
    font-weight: 700;
    font-size: 24px;
    line-height: 27px;
    color: var(--maroon);
    text-transform: uppercase;
  }
  .contact {
    position: absolute;
    left: 530px;
    top: 126px;
    list-style: none;
    color: var(--ink);
    font-weight: 600;
    font-size: 17px;
    line-height: 22.5px;
  }
  .background-square {
    position: absolute;
    left: 324px;
    top: 493px;
    width: 201px;
    height: 212px;
    border-radius: 22px;
    background: var(--mark-faint);
  }
  .bottom-band {
    position: absolute;
    left: 0;
    bottom: 0;
    width: 100%;
    height: 30px;
    background: var(--maroon);
  }
</style>
</head>
<body>
  <div class="letterhead">
    <svg class="top-arc" viewBox="0 0 849 120" aria-hidden="true">
      <path d="M0,114 C180,20 560,-10 849,80 L849,30 C560,-40 230,-30 0,104 Z" fill="var(--maroon)"/>
    </svg>

    <div class="brand">
      <div class="brand-square"></div>
      <div class="brand-name">Bramblewood<br>Lodging</div>
    </div>

    <ul class="contact">
      <li>ABN 87 592 104 316</li>
      <li>PO BOX 7816 , Tilbury Mail Centre</li>
      <li>QLD 4792</li>
      <li>EMAIL : dorian.platt@quillmail.net</li>
      <li>PHONE : 0438 172 964</li>
    </ul>

    <div class="background-square" aria-hidden="true"></div>

    <div class="bottom-band"></div>
  </div>
</body>
</html>
```